Business card design needed for rebranded top-end landscaping business

We need a new business card design, incorporating our logo (colours Green #8dc63f and Grey #8a8c8e) and also some options that include the colour dark navy (eg #000040) as our uniforms are navy with white and grey trim.

We are an innovative landscaping company that maintains high-end gardens for meticulous clients. We pride ourselves on our customer service, our professionalism, and our workmanship.

Our business name needs to be easily read and our branding needs to be bold and memorable, without screaming "tradesman"! We prefer clean lines over lots of fine detail.

The design MUST include:
- Business name ("Brambleton Gardenworks")
- Logo (file uploaded)
- Employee name
- Phone number
- Email address
- www.brambletongardenworks.com.au
- Facebook & Instagram logos
- The Turfcraft Guild logo (file uploaded) along with the word "Member"
- Licence "Lic. 618392K"

OPTIONAL inclusions:
- "Creating outdoor spaces for our community to be inspired, refreshed and re-energised"
- "Landscape Maintenance - Irrigation - Arboriculture" (dashes can be replaced with dots or other)
- "Fully qualified, licensed & insured"
- "Residential - Strata - Commercial - Real Estate" (dashes can be replaced with dots or other)

High-end professionals and retirees, real estate agents

Landscaping

See Project description

Sans Serif

Designer to choose colors to be used in the design.

• Must incorporate our logo, and colours Green #8dc63f and Grey #8a8c8e) from the logo, and the colour DARK NAVY (eg #000040).
• The design MUST include:
• - Business name ("Brambleton Gardenworks")
• - Logo (file uploaded)
• - Employee name
• - Phone number
• - Email address
• - www.brambletongardenworks.com.au
• - Facebook & Instagram logos
• - The Turfcraft Guild logo (file uploaded) along with the word "Member"
• - Licence "Lic. 618392K"
• OPTIONAL inclusions:
• - "Creating outdoor spaces for our community to be inspired, refreshed and re-energised"
• - "Landscape Maintenance - Irrigation - Arboriculture" (dashes can be replaced with dots or other)
• - "Fully qualified, licensed & insured"
• - "Residential - Strata - Commercial - Real Estate" (dashes can be replaced with dots or other)

```html
<!DOCTYPE html>
<html lang="en">
<head>
<meta charset="utf-8">
<title>Brambleton Gardenworks – Business Card</title>
<link rel="stylesheet" href="https://fonts.googleapis.com/css2?family=Roboto:wght@400;500;700&display=swap">
<style>
  :root {
    --brand-green: #8dc63f;
    --brand-grey: #8a8c8e;
    --text-grey: #6d6e70;
    --card-white: #ffffff;
    --backdrop: #f1f1f1;
  }
  * { margin: 0; padding: 0; box-sizing: border-box; }
  html, body { width: 1200px; height: 800px; overflow: hidden; }
  body {
    background: var(--backdrop);
    font-family: "Roboto", Arial, sans-serif;
    position: relative;
  }
  .card {
    position: absolute;
    width: 566px;
    height: 330px;
    box-shadow: 0 2px 6px rgba(0,0,0,0.12);
  }

  /* Front side */
  .card-front { left: 475px; top: 32px; background: var(--card-white); }
  .brand-block {
    position: absolute;
    left: 22px; top: 90px;
    width: 210px;
    text-align: center;
  }
  .brand-dot {
    display: block;
    width: 46px; height: 46px;
    margin: 0 auto 12px;
    border-radius: 50%;
    background: var(--brand-green);
  }
  .brand-name {
    color: var(--brand-grey);
    font-weight: 700;
    font-size: 23px;
    line-height: 1.1;
  }
  .divider {
    position: absolute;
    left: 243px; top: 99px;
    width: 2px; height: 128px;
    background: var(--brand-grey);
  }
  .contact {
    position: absolute;
    left: 264px; top: 99px;
    color: var(--text-grey);
  }
  .person-name {
    color: var(--brand-green);
    font-weight: 500;
    font-size: 20px;
    letter-spacing: 0.5px;
    text-transform: uppercase;
  }
  .person-role { font-size: 19px; margin-top: 2px; }
  .licence { font-size: 14px; margin-top: 12px; }
  .contact-list { list-style: none; margin-top: 6px; }
  .contact-list li {
    display: flex; align-items: center;
    font-size: 14px; line-height: 20px;
  }
  .contact-list svg { width: 11px; height: 11px; margin-right: 6px; fill: var(--brand-green); }
  .social {
    position: absolute;
    left: 0; right: 0; top: 276px;
    display: flex; justify-content: center; gap: 16px;
    font-size: 13.5px; color: var(--text-grey);
  }
  .social span { display: flex; align-items: center; }
  .social-mark {
    width: 10px; height: 10px; margin-right: 6px;
    background: var(--brand-green);
  }

  /* Back side */
  .card-back { left: 170px; top: 405px; background: var(--brand-green); }
  .back-name {
    position: absolute;
    right: 36px; top: 228px;
    color: var(--card-white);
    font-weight: 700;
    font-size: 31px;
    line-height: 1.05;
    text-align: center;
  }
  .back-name small { display: block; font-size: 17px; letter-spacing: 2px; text-transform: uppercase; }
</style>
</head>
<body>

<section class="card card-front" aria-label="Business card front">
  <div class="brand-block">
    <span class="brand-dot"></span>
    <p class="brand-name">Brambleton<br>Gardenworks</p>
  </div>
  <div class="divider"></div>
  <div class="contact">
    <p class="person-name">Owen Carlisle</p>
    <p class="person-role">Director</p>
    <p class="licence">Licence Lic. 618392K</p>
    <ul class="contact-list">
      <li><svg viewBox="0 0 24 24"><path d="M6.6 10.8a15 15 0 0 0 6.6 6.6l2.2-2.2c.3-.3.7-.4 1-.2 1.1.4 2.3.6 3.6.6.6 0 1 .4 1 1V20c0 .6-.4 1-1 1A17 17 0 0 1 3 4c0-.6.4-1 1-1h3.5c.6 0 1 .4 1 1 0 1.3.2 2.5.6 3.6.1.3 0 .7-.2 1z"/></svg>0400 318 742</li>
      <li><svg viewBox="0 0 24 24"><path d="M2 5h20v14H2z M2 5l10 8 10-8" stroke="#fff" stroke-width="1.5"/></svg>info@brambletongardenworks.com.au</li>
      <li><svg viewBox="0 0 24 24"><circle cx="12" cy="12" r="10"/><path d="M2 12h20M12 2c3 3 3 17 0 20M12 2c-3 3-3 17 0 20" stroke="#fff" stroke-width="1.5" fill="none"/></svg>www.brambletongardenworks.com.au</li>
    </ul>
  </div>
  <div class="social">
    <span><i class="social-mark"></i>brambletongardenworks</span>
    <span><i class="social-mark"></i>brambletongardenworks</span>
  </div>
</section>

<section class="card card-back" aria-label="Business card back">
  <p class="back-name">Brambleton<small>Gardenworks</small></p>
</section>

</body>
</html>
```